Corporate Design für Rechtsanwalt (Arbeitsrecht und Gesellschaftsrecht)
Zielgruppe
Rechtsanwalt (Arbeitsrecht und Gesellschaftsrecht)
Aufgabenstellung
Benötigt wird ein schlichtes und modernes Corporate Design für einen Anwalt, der sich vorwiegend mit Arbeitsrecht (Arbeitnehmer wie Arbeitgeber) und Gesellschaftsrecht befasst. Das Logo soll Professionalität und Seriosität vermitteln. Ein Paragraphenzeichen oder eine Waage sollen bitte nicht enthalten sein, da dies „alle“ Rechtsanwälte haben. Die Rechtsgebiete Arbeitsrecht und Gesellschaftsrecht sollen nicht im Logo enthalten sein.
Folgender Inhalt muss untergebracht werden:
Tobias Renz
Rechtsanwalt
Auf dem Briefkopf müssen Bankverbindung, St.-Nr., USt-ID, Internetadresse und Kontaktdaten (Adresse, Telefon, Fax und Mailadresse) untergebracht werden. Diese Daten müssen selbstständig abänderbar sein.
Notwendig sind: Logo, Briefkopf und Visitenkarte.

```html
<!DOCTYPE html>
<html lang="de">
<head>
<meta charset="utf-8">
<title>Tobias Renz – Rechtsanwalt – Geschäftsausstattung</title>
<link href="https://fonts.googleapis.com/css2?family=Montserrat:wght@300;400;500&family=Open+Sans:wght@400;600;700&display=swap" rel="stylesheet">
<style>
  :root {
    --backdrop: #6c6f72;
    --paper: #fafafa;
    --card: #ffffff;
    --ink: #3a3a3c;
    --text: #222222;
    --accent: #234a85;
  }
  * { margin: 0; padding: 0; box-sizing: border-box; }
  html, body { width: 1200px; height: 960px; overflow: hidden; }
  body { background: var(--backdrop); position: relative; font-family: "Open Sans", sans-serif; color: var(--text); }

  /* Briefbogen */
  .letter { position: absolute; left: 91px; top: 135px; width: 509px; height: 705px; background: var(--paper); }
  .letter .brand { position: absolute; left: 65px; top: 84px; width: 154px; text-align: center; }
  .brand-mark { display: block; width: 14px; height: 14px; background: var(--ink); margin: 0 auto 6px; }
  .brand-name { font-family: "Montserrat", sans-serif; font-weight: 500; color: var(--ink); letter-spacing: 0.14em; white-space: nowrap; }
  .brand-tag { font-family: "Montserrat", sans-serif; font-weight: 400; color: var(--ink); white-space: nowrap; }
  .letter .brand-name { font-size: 15px; }
  .letter .brand-tag { font-size: 5.5px; letter-spacing: 0.55em; margin-top: 3px; }
  .letter .divider { position: absolute; left: 298px; top: 27px; width: 2px; height: 93px; background: var(--ink); }
  .letter .contact { position: absolute; left: 310px; top: 46px; font-size: 8px; font-weight: 700; letter-spacing: 0.1em; line-height: 10.6px; color: var(--text); }
  .recipient { position: absolute; left: 64px; top: 163px; font-size: 7.5px; line-height: 11px; }
  .salutation { position: absolute; left: 64px; top: 255px; font-size: 9.5px; font-weight: 700; }
  .body-copy { position: absolute; left: 64px; top: 284px; width: 392px; font-size: 8.4px; line-height: 16px; }
  .body-copy p + p { margin-top: 16px; }
  .closing { position: absolute; left: 64px; top: 547px; font-size: 9.5px; font-weight: 700; line-height: 17px; }
  .letter-footer { position: absolute; left: 0; right: 0; top: 667px; text-align: center; font-size: 9px; font-weight: 700; word-spacing: 10px; }

  /* Visitenkarte Vorderseite */
  .card-front { position: absolute; left: 725px; top: 198px; width: 339px; height: 218px; background: var(--card); text-align: center; }
  .card-front .brand-mark { width: 28px; height: 28px; margin: 52px auto 36px; }
  .card-front .brand-name { font-size: 25px; letter-spacing: 0.12em; }
  .card-front .brand-tag { font-size: 10px; letter-spacing: 0.75em; margin-top: 8px; padding-left: 0.75em; }

  /* Visitenkarte Rückseite */
  .card-back { position: absolute; left: 642px; top: 552px; width: 505px; height: 287px; background: var(--card); }
  .frame-top { position: absolute; left: 28px; top: 29px; width: 174px; height: 173px; border-top: 1.5px solid var(--ink); border-left: 1.5px solid var(--ink); }
  .frame-bottom { position: absolute; left: 304px; top: 86px; width: 174px; height: 173px; border-bottom: 1.5px solid var(--ink); border-right: 1.5px solid var(--ink); }
  .card-back .divider { position: absolute; left: 238px; top: 58px; width: 1.5px; height: 172px; background: var(--ink); }
  .card-back .panel-square { position: absolute; left: 92px; top: 110px; width: 56px; height: 56px; background: var(--ink); }
  .card-back .brand { position: absolute; left: 268px; top: 74px; width: 180px; text-align: center; }
  .card-back .brand-name { font-size: 17px; }
  .card-back .brand-tag { font-size: 7px; letter-spacing: 0.6em; margin-top: 4px; padding-left: 0.6em; }
  .card-contact { position: absolute; left: 269px; top: 150px; font-family: "Montserrat", sans-serif; font-weight: 300; font-size: 14px; line-height: 25px; color: var(--text); }
</style>
</head>
<body>

<section class="letter" aria-label="Briefbogen">
  <div class="brand">
    <span class="brand-mark"></span>
    <div class="brand-name">TOBIAS RENZ</div>
    <div class="brand-tag">RECHTSANWALT</div>
  </div>
  <div class="divider"></div>
  <address class="contact" style="font-style:normal">
    Lindenallee 12<br>
    45678 Beispielstadt<br>
    Tel.: (0555) 0123-45<br>
    info@kanzlei-renz.example<br>
    www.kanzlei-renz.example
  </address>

  <div class="recipient">Herr<br>Jonas Beispiel<br>Ahornweg 4<br>12345 Feldhausen</div>

  <div class="salutation">Lieber Herr Lindner,</div>

  <div class="body-copy">
    <p>Ein Briefkopf ist die Kopfzeile am oberen Rand eines Briefpapiers. Die Kopfzeile enthält normalerweise einen Namen und eine Adresse, ein Logo oder Firmen-Design und manchmal ein Hintergrundmuster. Der Begriff „Briefkopf“ wird oft im Zusammenhang mit einem Brief verwendet, um die Kopfzeile bzw. den oberen Bereich eines Briefes in Szene zu setzen.</p>
    <p>Viele Unternehmen und Einzelpersonen bevorzugen es, einen Briefkopf anhand einer Vorlage in einem Textverarbeitungsprogramm oder einer Software-Anwendung zu erstellen. Eine solche Vorlage enthält die gleichen Informationen wie vorgedrucktes Briefpapier, es entstehen aber keine zusätzlichen Kosten. Der Briefkopf kann dann je nach Bedarf auf Briefpapier (oder ein leeres Blatt Papier) auf einem Drucker gedruckt oder elektronisch versendet werden.</p>
    <p>Der Begriff „Briefkopf“ wird oft im Zusammenhang mit einem Brief verwendet, um die Kopfzeile bzw. den oberen Bereich eines Briefes in Szene zu setzen.</p>
  </div>

  <div class="closing">Mit freundlichen Grüßen,<br>Tobias Renz</div>

  <div class="letter-footer">Bankverbindung, St.-Nr., USt-ID</div>
</section>

<section class="card-front" aria-label="Visitenkarte Vorderseite">
  <span class="brand-mark"></span>
  <div class="brand-name">TOBIAS RENZ</div>
  <div class="brand-tag">RECHTSANWALT</div>
</section>

<section class="card-back" aria-label="Visitenkarte Rückseite">
  <div class="frame-top"></div>
  <div class="panel-square"></div>
  <div class="divider"></div>
  <div class="frame-bottom"></div>
  <div class="brand">
    <div class="brand-name">TOBIAS RENZ</div>
    <div class="brand-tag">RECHTSANWALT</div>
  </div>
  <div class="card-contact">
    +49 555 0123-45<br>
    Lindenallee 12, Beispielstadt<br>
    hallo@kanzlei-renz.example
  </div>
</section>

</body>
</html>
```